I need to redesign my landing page into a high converting landing page adding 3 new elements

I need to redesign my landing page using all the same content, images etc. on the current page https://www.brightlanepromoworks.biz/travel_agency but also adding three new elements to the new redesign.

Please be sure to use my current header and footer from my current website since I will just plug the new design into it...

The Three New Elements Are Below (add these 3 new elements in addition to the current content)

1. Add a video element with this content:
Watch Below To See How Your Industry Uses Our Incentives To Skyrocket Their Sales!

2. Add the element of the 6 types of incentives they can offer.
You can use the same content and images that we use in this module on the homepage at www.brightlanepromoworks.biz ATTACHED IMAGE BUT YOU CAN FIND THE ORIGINAL IMAGES ON HOMEPAGE

3. Add 1 more call to action to give website visitors two choices:
A. Sign Up For 14 Days Risk Free
OR
B. Book A Live Call

Target Market(s)

Travel agents and travel advisors

Industry/Entity Type

marketing

Requirements
Must have
• HIGH CONVERTING LANDING PAGE
Nice to have
• short and to the point...no fluff

```html
<!DOCTYPE html>
<html lang="en">
<head>
<meta charset="utf-8">
<title>Brightlane Promo Works – Travel Agency Incentives</title>
<link href="https://fonts.googleapis.com/css2?family=Poppins:wght@400;500;600;700&family=Montserrat:wght@500;700;800;900&family=Allura&display=swap" rel="stylesheet">
<style>
:root{
  --navy:#27207a;
  --navy-deep:#1b1560;
  --blue:#1f64c4;
  --blue-mid:#2f78d0;
  --purple:#2c2090;
  --teal:#2fb795;
  --green:#22d40e;
  --ink:#3a3a3a;
  --grey:#666;
  --footer:#1e2833;
  --white:#fff;
}
*{box-sizing:border-box;margin:0;padding:0}
html,body{width:1200px;height:5338px;overflow:hidden}
body{font-family:'Poppins',sans-serif;color:var(--ink);background:var(--white);position:relative}
.abs{position:absolute}
section,header,footer{position:absolute;left:0;width:1200px}
.btn{position:absolute;display:flex;align-items:center;justify-content:center;font-family:'Montserrat',sans-serif;font-weight:700;font-size:14px;color:#fff;text-transform:uppercase;border-radius:4px}
.btn-blue{background:var(--blue-mid);border:2px solid #fff}
.btn-dark{background:#333;border:2px solid #fff}

/* header */
.topbar{top:0;height:68px;background:#fff}
.brand{position:absolute;left:124px;top:14px;display:flex;align-items:center;gap:10px;font-family:'Montserrat',sans-serif;font-weight:800;font-size:20px;color:var(--blue-mid);letter-spacing:.5px}
.brand .mark{width:34px;height:34px;border-radius:50%;background:var(--blue-mid)}
.account{position:absolute;right:124px;top:20px;display:flex;gap:28px;font-size:13px;font-weight:600;color:var(--navy)}
.account span{display:flex;align-items:center;gap:8px}
.account i{width:24px;height:24px;border:2px solid var(--green);border-radius:50%;display:inline-block}
.navbar{top:68px;height:42px;background:var(--navy)}
.navbar ul{list-style:none;display:flex;gap:24px;position:absolute;left:136px;top:12px;font-size:12.5px;font-weight:600;color:#fff}
.navbar .cta{position:absolute;left:773px;width:303px;top:0;height:42px;background:var(--green);display:flex;justify-content:space-around;align-items:center;font-size:12.5px;font-weight:600;color:var(--navy)}

/* hero */
.hero{top:110px;height:520px;background:linear-gradient(160deg,#7fc6d6 0%,#3fa88f 45%,#1d8a72 100%)}
.hero h1{position:absolute;left:108px;top:120px;font-family:'Montserrat',sans-serif;font-weight:900;font-size:42px;line-height:52px;color:#fff;text-transform:uppercase;letter-spacing:.5px}
.hero .dots{position:absolute;left:108px;top:424px;display:flex;gap:10px}
.hero .dots b{width:30px;height:4px;background:rgba(255,255,255,.6);border-radius:2px}
.hero .dots b.on{width:44px;background:#fff}
.hero svg{position:absolute;left:0;bottom:0}

/* incentives */
.incentives{top:630px;height:920px}
.incentives h2{position:absolute;left:83px;top:150px;font-family:'Montserrat',sans-serif;font-weight:500;font-size:32px;line-height:42px;color:#444;text-transform:uppercase}
.incentives h2 strong{color:var(--blue-mid);font-weight:900;display:block}
.incentives h2 strong+strong{margin-top:-2px}
.rule{position:absolute;height:3px;background:var(--blue-mid)}
.tile{position:absolute;width:332px;height:340px;box-shadow:0 6px 18px rgba(0,0,0,.15)}
.tile .photo{height:278px}
.tile .cap{height:62px;background:var(--blue-mid);color:#fff;font-size:19px;display:flex;align-items:center;justify-content:center}

/* ad packs */
.adpacks{top:1544px;height:740px}
.adpacks h2{position:absolute;width:100%;top:105px;text-align:center;font-family:'Montserrat',sans-serif;font-weight:500;font-size:33px;color:#fff}
.adpacks h2 strong{font-weight:900}
.adpacks p{position:absolute;width:100%;top:196px;text-align:center;font-size:14px;line-height:31px;color:#fff}
.ad{position:absolute;top:275px;height:320px}
.carousel-dots{position:absolute;top:600px;left:536px;display:flex;gap:14px}
.carousel-dots b{width:36px;height:4px;background:rgba(255,255,255,.5)}
.carousel-dots b.on{background:#fff;width:44px}

/* vouchers */
.vouchers{top:2280px;height:648px;background:linear-gradient(180deg,#2a1d8c,#2d2396 60%,#26207d)}
.vouchers h2{position:absolute;width:100%;top:110px;text-align:center;font-family:'Montserrat',sans-serif;font-weight:700;font-size:21px;color:#cfe24a;text-transform:uppercase}
.vouchers h2 em{font-style:normal;color:#fff}
.vouchers .sub{position:absolute;width:100%;top:140px;text-align:center;font-size:15px;font-weight:600;color:#fff}
.voucher{position:absolute;top:200px;width:180px;text-align:center;color:#fff}
.voucher .kind{font-size:18px;font-weight:600;line-height:22px}
.voucher .script{font-family:'Allura',cursive;font-size:28px;line-height:28px}
.voucher .art{width:124px;height:162px;margin:12px auto 0;border:3px solid #fff;box-shadow:0 0 14px rgba(255,220,120,.6)}
.voucher .label{margin-top:20px;font-size:14.5px;font-weight:600;line-height:22px}

/* video */
.video{top:2928px;height:702px}
.video h2{position:absolute;width:100%;top:68px;text-align:center;font-family:'Montserrat',sans-serif;font-weight:600;font-size:34px;line-height:44px;color:#444;text-transform:uppercase}
.video h2 strong{color:var(--blue-mid);font-weight:900}
.player{position:absolute;left:124px;top:226px;width:952px;height:373px;border-radius:40px;background:linear-gradient(180deg,#dfe8fb,#9fb6e8 70%,#5e84d0);overflow:hidden}
.player .frame{position:absolute;inset:18px 28px;border:3px solid #fff;border-radius:34px}
.player .play{position:absolute;left:452px;top:160px;width:56px;height:56px;border-radius:50%;background:rgba(120,120,120,.75)}

/* promo */
.promo{top:3630px;height:584px;background:var(--teal)}
.promo .photo{position:absolute;left:104px;top:69px;width:667px;height:424px;background:linear-gradient(180deg,#6fb6e6 0%,#a9d8f0 40%,#2aa9c4 65%,#138a9f 100%)}
.promo .card{position:absolute;left:719px;top:141px;width:456px;height:305px;background:#fff;border-radius:110px 0 0 110px;display:flex;align-items:center;justify-content:center;padding:0 36px 0 60px;text-align:center;font-size:19px;line-height:33px;color:#444}

/* testimonials */
.testimonials{top:4214px;height:593px}
.testimonials h2{position:absolute;width:100%;top:66px;text-align:center;font-family:'Montserrat',sans-serif;font-weight:500;font-size:32px;color:#444}
.testimonials h2 strong{color:var(--blue-mid);font-weight:900}
.quote{position:absolute;top:168px;width:530px;height:270px;background:#fff;box-shadow:0 2px 14px rgba(0,0,0,.12);padding:26px 26px 0}
.quote .qm{font-family:'Montserrat',sans-serif;font-weight:900;font-size:56px;line-height:44px;color:var(--blue-mid)}
.quote p{margin-top:18px;font-size:15px;line-height:29px;color:#555}
.quote .who{position:absolute;left:26px;top:206px;display:flex;align-items:center;gap:14px}
.quote .avatar{width:46px;height:46px;border-radius:50%}
.quote .name{font-weight:600;font-size:17px;color:#333}
.quote .stars{color:var(--blue-mid);font-size:17px;letter-spacing:2px}

/* footer */
.site-footer{top:4807px;height:531px;background:var(--footer);color:#fff}
.site-footer h4{font-family:'Montserrat',sans-serif;font-weight:800;font-size:15px;text-transform:uppercase;margin-bottom:20px}
.site-footer li{list-style:none;font-size:11px;line-height:26px;color:#e5e5e5}
.foot-brand{position:absolute;left:73px;top:60px;width:254px;text-align:center;font-family:'Montserrat',sans-serif;font-weight:800;font-size:22px;line-height:28px;color:var(--blue-mid);text-transform:uppercase}
.socials{position:absolute;left:105px;top:170px;display:flex;gap:14px}
.socials i{width:36px;height:36px;border-radius:50%;background:#666}
.foot-cta{position:absolute;left:73px;top:237px;width:252px;height:46px;border-radius:23px;background:var(--green);color:var(--navy);font-weight:700;font-size:12px;line-height:15px;text-align:center;display:flex;align-items:center;justify-content:center}
.contact{position:absolute;left:373px;top:62px;width:300px}
.contact .row{display:flex;gap:10px;font-size:11px;line-height:16px;margin-bottom:14px}
.contact .row svg{flex:none;margin-top:1px}
.contact .row b{font-weight:600}
.contact .hl{color:#f5a623}
.col{position:absolute;top:62px}
.legal{position:absolute;left:73px;right:36px;top:466px;border-top:1px solid #3c4754;padding-top:30px;display:flex;justify-content:space-between;font-size:11px;color:#cfd3d8}
.legal b{color:#fff}
</style>
</head>
<body>

<header class="topbar">
  <div class="brand"><span class="mark"></span>Brightlane Promo Works</div>
  <div class="account"><span><i></i>Login</span><span><i></i>Sign Up</span></div>
</header>

<nav class="navbar">
  <ul><li>Home</li><li>Incentives List</li><li>Get Free Samples</li><li>Integrations</li><li>Industries ▾</li></ul>
  <div class="cta"><span>Call or Text ▾</span><span>Book A Demo ▾</span></div>
</nav>

<section class="hero" role="img" aria-label="Tropical lagoon with a wooden outrigger boat on turquoise water">
  <h1>Imagine being able to<br>offer BOGO deals<br>with every booking!</h1>
  <div class="btn btn-blue" style="left:112px;top:286px;width:276px;height:42px">Sign up for 14 days risk free</div>
  <div class="btn btn-dark" style="left:414px;top:286px;width:184px;height:42px">Book a live call</div>
  <div class="dots"><b></b><b class="on"></b><b></b></div>
  <svg width="1200" height="90" viewBox="0 0 1200 90" preserveAspectRatio="none">
    <path d="M0 60 C300 10 700 90 1200 20 L1200 90 L0 90Z" fill="#fff"/>
    <path d="M0 52 C300 2 700 84 1200 12 L1200 26 C700 96 300 18 0 70Z" fill="#27207a"/>
  </svg>
</section>

<section class="incentives">
  <h2>Our marketing<br>incentives<strong>can help you</strong><strong>with</strong></h2>
  <div class="rule" style="left:83px;top:341px;width:142px"></div>

  <div class="tile" style="left:433px;top:81px"><div class="photo" role="img" aria-label="Swimmer in a clear cave lagoon" style="background:linear-gradient(180deg,#4b5a52,#2aa9b8 70%,#1a8ea0)"></div><div class="cap">Special Promotion giveaway</div></div>
  <div class="tile" style="left:787px;top:81px"><div class="photo" role="img" aria-label="Turquoise tropical shoreline under blue sky" style="background:linear-gradient(180deg,#7fb4e0,#a4d6ee 40%,#3fc4c4 60%,#1d8fa0)"></div><div class="cap">Referral Gifts</div></div>
  <div class="tile" style="left:83px;top:456px"><div class="photo" role="img" aria-label="Resort bedroom opening onto an ocean terrace" style="background:linear-gradient(90deg,#4a3b2e,#8c7460 45%,#74b5d4)"></div><div class="cap">Welcome Gifts</div></div>
  <div class="tile" style="left:433px;top:456px"><div class="photo" role="img" aria-label="Wooden stilt huts over a calm jungle lagoon" style="background:linear-gradient(180deg,#e6eef3,#3f6a3a 45%,#6c8c86)"></div><div class="cap">Enticement for booking a flight</div></div>
  <div class="tile" style="left:787px;top:456px"><div class="photo" role="img" aria-label="Blue boats moored in a bay" style="background:linear-gradient(180deg,#9fc3e0,#5c86a8 45%,#2e6a9a)"></div><div class="cap">Gifts for booking a Cruise</div></div>
</section>

<section class="adpacks">
  <svg class="abs" style="left:0;top:0" width="1200" height="740" viewBox="0 0 1200 740" preserveAspectRatio="none">
    <defs><linearGradient id="packsBg" x1="0" y1="0" x2="0" y2="1"><stop offset="0" stop-color="#2a6fca"/><stop offset="1" stop-color="#1d5fb8"/></linearGradient></defs>
    <path d="M0 30 C300 -10 800 70 1200 10 L1200 740 L0 740Z" fill="#27207a"/>
    <path d="M0 58 C300 18 800 98 1200 38 L1200 700 C800 640 400 740 0 690Z" fill="url(#packsBg)"/>
  </svg>
  <h2>PLUG IN <strong>PLAY AD PACKS</strong></h2>
  <div class="rule" style="left:540px;top:158px;width:120px;background:#fff"></div>
  <p>Proven Social Feed™ Ad Templates, High-Converting Banner Ad Templates To Use With The SearchWide™ Display Network Plus<br>Time-Tested Print Ad Templates That We Provide To You For Free With Your BPW Package.</p>

  <div class="ad" role="img" aria-label="Cruise ship ad template offering a free four night cruise" style="left:81px;width:292px;background:linear-gradient(135deg,#1a1408,#6b4a1a 60%,#c48a2c)"></div>
  <div class="ad" role="img" aria-label="Tour package ad template offering a free tablet" style="left:376px;top:316px;height:240px;width:350px;background:linear-gradient(90deg,#1f3f8a,#3f5fa8 60%,#c8a070);border:3px solid #fff"></div>
  <div class="ad" role="img" aria-label="Partially visible ad template" style="left:740px;top:316px;height:240px;width:80px;background:linear-gradient(90deg,#4a66b0,#d4a070)"></div>
  <div class="ad" role="img" aria-label="Partially visible ad template" style="left:826px;top:310px;height:250px;width:84px;background:linear-gradient(90deg,#eef2fa,#5f84c8)"></div>
  <div class="ad" role="img" aria-label="Tour package ad template offering a free smart fitness watch" style="left:914px;width:206px;background:linear-gradient(180deg,#2f58c0,#6a7ed8 55%,#3a4fb0)"></div>

  <div class="carousel-dots"><b></b><b class="on"></b><b></b></div>
  <div class="btn" style="left:462px;top:656px;width:276px;height:40px;border:2px solid #fff;font-size:13px">Sign up for 14 days risk free</div>
</section>

<section class="vouchers">
  <h2>Give away an unlimited amount of <em>complimentary gift vouchers</em> redeemable for:</h2>
  <div class="sub">(without having to personally fulfill or pay for any of them yourself!)</div>

  <div class="voucher" style="left:53px"><div class="kind">Hotel Saving</div><div class="script">Cards</div><div class="art" role="img" aria-label="Hotel savings card brochure" style="background:linear-gradient(180deg,#5a2a18,#b86a3a 50%,#e8d4b8)"></div><div class="label">Complimentary<br>$100–$500<br>Hotel Cards</div></div>
  <div class="voucher" style="left:233px"><div class="kind">Smart Device</div><div class="script">Certificates</div><div class="art" role="img" aria-label="Smart device certificate brochure" style="background:linear-gradient(180deg,#e8c23a,#f4e4a0 50%,#4a4a4a)"></div><div class="label">Complimentary<br>Smart<br>Devices</div></div>
  <div class="voucher" style="left:416px"><div class="kind">Restaurant</div><div class="script">Cards</div><div class="art" role="img" aria-label="Restaurant dining card brochure" style="background:linear-gradient(180deg,#7a1c1c,#c8583a 50%,#efe0d0)"></div><div class="label">Complimentary<br>$100–$500<br>Dining Cards</div></div>
  <div class="voucher" style="left:596px"><div class="kind">Airfare</div><div class="script">Vouchers</div><div class="art" role="img" aria-label="Airfare voucher brochure" style="background:linear-gradient(180deg,#c24a3a,#f0d8c8 50%,#e8ecf4)"></div><div class="label">Complimentary<br>Roundtrip<br>Airfare</div></div>
  <div class="voucher" style="left:778px"><div class="kind">Cruise</div><div class="script">Certificates</div><div class="art" role="img" aria-label="Cruise certificate brochure" style="background:linear-gradient(180deg,#3a66b0,#dfe6f4 50%,#c84a3a)"></div><div class="label">Complimentary<br>Cruise<br>Getaways</div></div>
  <div class="voucher" style="left:959px"><div class="kind">Resort</div><div class="script">Certificates</div><div class="art" role="img" aria-label="All-inclusive resort certificate brochure" style="background:linear-gradient(180deg,#d85a2a,#f3e2c8 50%,#3aa0b8)"></div><div class="label">Complimentary<br>All-Inclusive<br>Vacations</div></div>

  <div class="btn btn-blue" style="left:446px;top:547px;width:310px;height:43px;font-size:13.5px">Sign up for 14 days risk free</div>
</section>

<section class="video">
  <h2>Watch below to see how your industry uses our<br><strong>incentives to skyrocket their sales!</strong></h2>
  <div class="rule" style="left:530px;top:176px;width:140px"></div>
  <div class="player" role="img" aria-label="Video preview of a cruise ship at sea advertising a four night cruise">
    <div class="frame"></div>
    <div class="play"></div>
    <svg class="abs" style="left:472px;top:176px" width="22" height="24" viewBox="0 0 22 24"><path d="M2 1 L21 12 L2 23Z" fill="#fff"/></svg>
  </div>
</section>

<section class="promo">
  <div class="photo" role="img" aria-label="Thatched overwater bungalow with sun loungers on a turquoise lagoon"></div>
  <div class="card">Attract More New Customers Giving Away Free Vacation Certificates, Cruise Vouchers, Smart Devices, Dining Takeout Vouchers And More. You'll Never Pay For A Single Certificate, Vacation or Any Item, Ever.</div>
</section>

<section class="testimonials">
  <h2>CLIENT <strong>TESTIMONIALS</strong></h2>
  <div class="rule" style="left:540px;top:122px;width:120px"></div>
  <div class="quote" style="left:58px">
    <div class="qm">“</div>
    <p>Brightlane Promo Works has helped my massage business grow exponentially in the last 2 years. It is the easiest and most-affordable way to reward loyal customers, as well as, employees!</p>
    <div class="who"><div class="avatar" role="img" aria-label="Client portrait" style="background:#a08070"></div><div><div class="name">Marla.K</div><div class="stars">★★★★★</div></div></div>
  </div>
  <div class="quote" style="left:613px">
    <div class="qm">“</div>
    <p>I was so happy to hear from one of our clients who was thrilled after she redeemed her certificate for a four-night hotel stay. She got the date she wanted and the hotel she chose. She has two kids and she got a three-bedroom town</p>
    <div class="who"><div class="avatar" role="img" aria-label="Client portrait" style="background:#c89a78"></div><div><div class="name">Donna .R</div><div class="stars">★★★★★</div></div></div>
  </div>
  <div class="btn" style="left:501px;top:483px;width:197px;height:40px;background:var(--blue-mid);font-size:13.5px">View all reviews</div>
</section>

<footer class="site-footer">
  <div class="foot-brand">Brightlane<br>Promo Works</div>
  <div class="socials"><i></i><i></i><i></i><i></i></div>
  <div class="foot-cta">SIGN UP FOR A 14 DAY RISK<br>FREE TRIAL</div>

  <div class="contact">
    <h4>Contact Us</h4>
    <div class="row"><svg width="12" height="14" viewBox="0 0 12 14"><path d="M6 1a4.5 4.5 0 0 0-4.5 4.5C1.5 9 6 13 6 13s4.5-4 4.5-7.5A4.5 4.5 0 0 0 6 1z" fill="none" stroke="#fff"/><circle cx="6" cy="5.5" r="1.5" fill="#fff"/></svg><div><b>Brightlane Promo Works Group, Inc.</b><br>2240 Harbor View Rd #410<br>Seabrook, CA 90811</div></div>
    <div class="row"><svg width="12" height="12" viewBox="0 0 12 12"><rect x="1" y="2" width="10" height="9" rx="1" fill="none" stroke="#fff"/><path d="M1 5h10" stroke="#fff"/></svg><div><b>Book A Demo:</b><br>New Sales<br>Current/Past Clients</div></div>
    <div class="row"><svg width="12" height="12" viewBox="0 0 12 12"><path d="M3 1l2 3-1.5 1.2a6 6 0 0 0 3.3 3.3L8 7l3 2-1 2C5 11 1 7 1 2z" fill="none" stroke="#fff"/></svg><div><b>Call Or Text Us:</b><br>New Sales 1-555-010-4181<br>Current/Past Clients 1-555-010-9633</div></div>
    <div class="row"><svg width="12" height="12" viewBox="0 0 12 12"><rect x="1" y="2.5" width="10" height="7" fill="none" stroke="#fff"/><path d="M1 2.5l5 4 5-4" fill="none" stroke="#fff"/></svg><div>support@brightlanepromoworks.com</div></div>
    <div class="row"><svg width="12" height="12" viewBox="0 0 12 12"><circle cx="6" cy="6" r="5" fill="none" stroke="#fff"/><path d="M6 3v3l2 1" fill="none" stroke="#fff"/></svg><div><b>SMS, Email &amp; Online Support:</b><br>Monday - Friday <span class="hl">8am - 5pm PST</span><br><span class="hl">Sat/Sun/Holidays Closed</span><br>*After Hours All Inquiries Will Be Replied To On The Next Business Day.</div></div>
  </div>

  <div class="col" style="left:715px">
    <h4>Quick Links</h4>
    <ul><li>Home</li><li>The Incentives</li><li>Login</li><li>Sign Up</li><li>Affiliate</li><li>Integrations</li><li>Testimonials</li><li style="line-height:16px;padding:5px 0">Frequently Asked<br>Questions</li><li style="line-height:16px;padding:5px 0">BPW Distribute Certificate<br>Demo Videos</li><li style="line-height:16px;padding:5px 0">White Label Agency<br>Program</li></ul>
  </div>
  <div class="col" style="left:920px">
    <h4>Other Links</h4>
    <ul><li>Hoteliers</li><li>BPW Certificates List</li><li>How To Use BPW Certificates</li><li>Pop Ups &amp; Sticky Bars</li><li>Whitepaper - Increase Sales</li><li style="line-height:16px;padding:5px 0">Whitepaper - Improve Sales During<br>Strange Times</li><li style="line-height:16px;padding:5px 0">Whitepaper - Boost Website<br>Conversions</li></ul>
  </div>

  <div class="legal"><span>© 2024 <b>Brightlane Promo Works Group, Inc.</b> All Rights Reserved.</span><span>Privacy Policy &nbsp;|&nbsp; Term And Conditions &nbsp;&nbsp; <b>C75</b></span></div>
</footer>

</body>
</html>
```